Business Card Design for company

We want new business cards. We'd like something different-- yet still highly professional. Our tagline is Providing leadership, delivering success. Stock photos are ok, as long as they are relevant and look upscale.

Target Market(s)

Architecture/Business Management Consulting/Engineering Consulting

Contact Information for Business Card

dark gray background with pops of blue might be good, but you tell me. You're the designers. Rounded corners might be nice, but again, you tell me.

Font styles to use
Serif
Sans Serif

Colors
3276b5
5c5c5c
9d9d9d
fbfbfb

Requirements
Nice to have
• Something different, but still very professional.

```html
<!DOCTYPE html>
<html lang="en">
<head>
<meta charset="utf-8">
<title>Corvane International – Business Card</title>
<link rel="stylesheet" href="https://fonts.googleapis.com/css2?family=Montserrat:wght@600;700&family=Open+Sans:wght@400;600&display=swap">
<style>
  :root {
    --brand-blue: #3276b5;
    --deep-blue: #2c5f96;
    --charcoal: #4a4d52;
    --mid-gray: #5c5c5c;
    --light-gray: #9d9d9d;
    --paper: #fbfbfb;
    --stage: #e6e7e9;
  }
  * { box-sizing: border-box; margin: 0; padding: 0; }
  html, body { width: 1200px; height: 782px; overflow: hidden; }
  body {
    background: var(--stage);
    display: flex;
    flex-direction: column;
    align-items: center;
    justify-content: center;
    gap: 40px;
    font-family: "Open Sans", Arial, sans-serif;
  }
  .card {
    position: relative;
    width: 560px;
    height: 320px;
    overflow: hidden;
    box-shadow: 0 6px 18px rgba(0,0,0,.18);
  }

  /* Back side */
  .card-back { background: var(--deep-blue); }
  .card-back .pattern-field {
    position: absolute; inset: 0;
    background: linear-gradient(160deg, #3468a1 0%, var(--deep-blue) 100%);
  }
  .card-back .back-wordmark {
    position: absolute;
    left: 330px; top: 178px;
    font-family: "Montserrat", Arial, sans-serif;
    font-weight: 700;
    font-size: 30px;
    color: var(--paper);
    letter-spacing: 1px;
  }

  /* Front side */
  .card-front { background: var(--paper); }
  .holder { position: absolute; left: 34px; top: 30px; }
  .holder-name {
    font-family: "Montserrat", Arial, sans-serif;
    font-weight: 700;
    font-size: 17px;
    letter-spacing: .3px;
    color: var(--charcoal);
  }
  .holder-name .first { color: var(--brand-blue); }
  .holder-title { font-size: 12px; color: var(--mid-gray); margin-top: 1px; }

  .contact-list {
    position: absolute; left: 34px; top: 176px;
    list-style: none;
    font-size: 13px;
    line-height: 19px;
    color: #2b2b2b;
  }
  .contact-list li { display: flex; align-items: center; gap: 8px; }
  .contact-list svg { width: 11px; height: 11px; fill: var(--brand-blue); flex: none; }

  .front-wordmark {
    position: absolute; left: 318px; top: 118px;
    display: flex; align-items: center; gap: 10px;
    font-family: "Montserrat", Arial, sans-serif;
    font-weight: 700;
    font-size: 28px;
    color: var(--charcoal);
    letter-spacing: 1px;
  }
  .front-wordmark .mark-square { width: 16px; height: 16px; background: var(--brand-blue); }

  .address {
    position: absolute; right: 30px; top: 228px;
    text-align: right;
    font-size: 13px;
    line-height: 18px;
    color: #2b2b2b;
  }
  .bands { position: absolute; left: 0; bottom: 0; width: 560px; height: 320px; pointer-events: none; }
</style>
</head>
<body>

  <section class="card card-back" aria-label="Card back">
    <div class="pattern-field" role="img" aria-label="Repeated company wordmark pattern in tonal blue"></div>
    <div class="back-wordmark">CORVANE</div>
  </section>

  <section class="card card-front" aria-label="Card front">
    <div class="holder">
      <div class="holder-name"><span class="first">DANIEL</span> MARSH</div>
      <div class="holder-title">Managing Director</div>
    </div>

    <ul class="contact-list">
      <li><svg viewBox="0 0 24 24"><path d="M6.6 10.8a15.5 15.5 0 0 0 6.6 6.6l2.2-2.2c.3-.3.7-.4 1-.2 1.1.4 2.3.6 3.6.6.6 0 1 .4 1 1V20c0 .6-.4 1-1 1A17 17 0 0 1 3 4c0-.6.4-1 1-1h3.5c.6 0 1 .4 1 1 0 1.3.2 2.5.6 3.6.1.3 0 .7-.2 1z"/></svg>010-555 246 810</li>
      <li><svg viewBox="0 0 24 24"><path d="M7 1h10a2 2 0 0 1 2 2v18a2 2 0 0 1-2 2H7a2 2 0 0 1-2-2V3a2 2 0 0 1 2-2zm0 3v14h10V4zm5 15.5a1 1 0 1 0 0 2 1 1 0 0 0 0-2z"/></svg>010-555 246 811</li>
      <li><svg viewBox="0 0 24 24"><path d="M2 5h20v14H2zm2 2v.5l8 5 8-5V7zm0 3v7h16v-7l-8 5z"/></svg>info@corvane.com</li>
      <li><svg viewBox="0 0 24 24"><circle cx="12" cy="12" r="10"/></svg>www.corvane.com</li>
    </ul>

    <div class="front-wordmark"><span class="mark-square"></span>CORVANE</div>

    <div class="address">12345, Address Goes Here<br>Country Name, 123456</div>

    <svg class="bands" viewBox="0 0 560 320" aria-hidden="true">
      <polygon points="0,306 258,306 253,320 0,320" fill="var(--brand-blue)"/>
      <polygon points="276,290 560,290 560,320 266,320" fill="var(--charcoal)"/>
    </svg>
  </section>

</body>
</html>
```